Tech business card design

We need an amazing business card design for our new business 'Brakka' a marketing tech startup based in Sydney, Australia. We provide an online marketplace for businesses to search and buy advertising media, connect with service providers and learn more about marketing. We wish to communicate 'cool tech', reliability and professionalism and design based around our logo.

Target Market(s)

Business Owners

Contact Information for Business Card

Name
Position
Email Address
Website
Phone Number

Font styles to use
Other font styles liked:
• Avenir & Avenir Next

Colors

Designer to choose colors to be used in the design.

```html
<!DOCTYPE html>
<html lang="en">
<head>
<meta charset="utf-8">
<title>Brakka Business Card</title>
<link rel="stylesheet" href="https://fonts.googleapis.com/css2?family=Nunito+Sans:wght@400;600;800&display=swap">
<style>
  :root {
    --page: #e7e7e9;
    --paper: #ededed;
    --navy: #12133a;
    --navy-band: #1a1b44;
    --white: #f4f4f6;
  }
  * { margin: 0; padding: 0; box-sizing: border-box; }
  html, body {
    width: 1200px; height: 1200px; overflow: hidden;
    background: var(--page);
    font-family: "Nunito Sans", "Avenir Next", Avenir, sans-serif;
  }
  .card {
    position: absolute;
    left: 228px;
    width: 744px; height: 424px;
    border-radius: 36px;
    overflow: hidden;
  }
  .card--front { top: 136px; background: var(--paper); color: var(--navy); }
  .card--back  { top: 640px; background: var(--navy); }

  .wordmark {
    position: absolute; left: 0; right: 0;
    text-align: center;
    font-weight: 800;
    font-size: 124px;
    line-height: 1;
    letter-spacing: -2px;
  }
  .card--front .wordmark { top: 40px; color: var(--navy); }
  .card--back .wordmark  { top: 142px; color: var(--white); }

  .person { position: absolute; left: 0; right: 0; top: 226px; text-align: center; }
  .person__name { font-size: 29px; font-weight: 600; line-height: 1.2; }
  .person__role { font-size: 23px; font-weight: 400; line-height: 1.3; }

  .contacts {
    position: absolute; left: 0; right: 0; top: 306px;
    display: flex; justify-content: center; align-items: center; gap: 14px;
    font-size: 20px;
  }
  .contact { display: flex; align-items: center; gap: 10px; }
  .contact svg { width: 18px; height: 18px; display: block; }

  .band { position: absolute; left: 0; top: 0; width: 744px; height: 424px; }
  .website {
    position: absolute; left: 0; right: 0; top: 384px;
    text-align: center; color: #d8d8e2; font-size: 18px; letter-spacing: 0.3px;
  }
</style>
</head>
<body>
  <section class="card card--front">
    <div class="wordmark">Brakka</div>
    <div class="person">
      <div class="person__name">Liam Carter</div>
      <div class="person__role">Founder, Director</div>
    </div>
    <div class="contacts">
      <span class="contact">
        <svg viewBox="0 0 18 18" aria-hidden="true">
          <circle cx="9" cy="9" r="9" fill="var(--navy)"/>
          <path d="M5 7.5c0-1.5 1.8-2.5 4-2.5s4 1 4 2.5l-1.6.5-.6-1.3H7.2l-.6 1.3z M5.5 12.5l1.2-4h4.6l1.2 4z" fill="var(--paper)"/>
        </svg>
        +61 (0)400 555 218
      </span>
      <span class="contact">
        <svg viewBox="0 0 18 18" aria-hidden="true">
          <circle cx="9" cy="9" r="9" fill="var(--navy)"/>
          <rect x="4.5" y="6" width="9" height="6.5" rx="0.8" fill="var(--paper)"/>
          <path d="M4.8 6.4 9 9.6l4.2-3.2" fill="none" stroke="var(--navy)" stroke-width="1"/>
        </svg>
        liam@brakkamedia.com.au
      </span>
    </div>
    <svg class="band" viewBox="0 0 744 424" aria-hidden="true">
      <path d="M0 424 L0 412 Q372 330 744 412 L744 424 Z" fill="var(--navy-band)"/>
    </svg>
    <div class="website">www.brakkamedia.com.au</div>
  </section>

  <section class="card card--back">
    <div class="wordmark">Brakka</div>
  </section>
</body>
</html>
```